48207 Velmont Lane Ad (for Facebook and Instagram)

Ad to run on Social Media (i.e. Facebook, Instagram etc.)
to advertise sale of property.

Target Market(s)

Prospective Buyers

Requirements
Must have
• TEXT
• Presenting
• 48207 Velmont Lane, Brandywine, MD
• Priced to Sell
• 5 Bedroom / 4 Bathroom Colonial with Contemporary Design and Charm
• Over 5,000 sq ft of Spacious Elegance
• Extraordinary Master Bedroom with Spacious Bath
• Modern Open Concept Kitchen
• Natural Oak Floors
• Stainless Steel Appliances
• Granite Counter-Tops
• Exterior with Outdoor Security, Design Lighting and Sprinkler System
• Just 10 Minutes From Corwen Quay
• Call Marcus Pendley, Realtor
• Tolbrook Realty Inc.
• Phone (240) 555-0187
• Email - premierhomedesk@mailbrook.test

```html
<!DOCTYPE html>
<html lang="en">
<head>
<meta charset="utf-8">
<title>48207 Velmont Lane – For Sale</title>
<link rel="stylesheet" href="https://fonts.googleapis.com/css2?family=Montserrat:wght@300;600;700;800;900&family=Roboto:wght@400;500;700&display=swap">
<style>
  :root {
    --blue-deep: #0a2a86;
    --blue-mid: #0f5fbf;
    --blue-bright: #1a8ad8;
    --band-blue: #0e6cc4;
    --name-blue: #0f6fc6;
    --ink: #2b2b2b;
    --panel-grey: #eceff2;
    --paper: #fbfcfe;
    --backdrop: #e2e2e2;
  }
  html, body {
    margin: 0;
    width: 1200px;
    height: 1200px;
    overflow: hidden;
    background: var(--backdrop);
  }
  .ad {
    position: absolute;
    left: 60px;
    top: 0;
    width: 1080px;
    height: 1200px;
    display: block;
  }
  .headline { font-family: "Montserrat", sans-serif; font-weight: 900; fill: #fff; }
  .presenting { font-family: "Montserrat", sans-serif; font-weight: 700; fill: #fff; font-size: 14px; }
  .address { font-family: "Roboto", sans-serif; font-weight: 400; fill: #fff; font-size: 18px; }
  .band-label { font-family: "Roboto", sans-serif; font-weight: 500; fill: #fff; font-size: 21px; }
  .price { font-family: "Montserrat", sans-serif; font-weight: 800; fill: #fff; font-size: 30px; }
  .brokerage { font-family: "Montserrat", sans-serif; font-weight: 700; fill: #fff; font-size: 22px; }
  .email { font-family: "Montserrat", sans-serif; font-weight: 300; fill: #fff; font-size: 17px; }
  .agent-name { font-family: "Roboto", sans-serif; font-weight: 700; fill: var(--name-blue); font-size: 26px; }
  .agent-title { font-family: "Roboto", sans-serif; font-weight: 400; fill: var(--ink); font-size: 16px; }
  .agent-phone { font-family: "Roboto", sans-serif; font-weight: 700; fill: var(--ink); font-size: 27px; }
  .brand-name { font-family: "Roboto", sans-serif; font-weight: 700; fill: var(--blue-deep); font-size: 22px; }
  .section-title { font-family: "Roboto", sans-serif; font-weight: 500; fill: #fff; font-size: 25px; }
  .feature { font-family: "Roboto", sans-serif; font-weight: 400; fill: var(--ink); font-size: 18.5px; }
  .tick { fill: none; stroke: var(--ink); stroke-width: 2.4; stroke-linecap: round; stroke-linejoin: round; }
</style>
</head>
<body>
<svg class="ad" viewBox="0 0 833 926" xmlns="http://www.w3.org/2000/svg">
  <defs>
    <linearGradient id="hero-blue" x1="1" y1="0" x2="0" y2="1">
      <stop offset="0" stop-color="var(--blue-bright)"/>
      <stop offset="0.55" stop-color="var(--blue-mid)"/>
      <stop offset="1" stop-color="var(--blue-deep)"/>
    </linearGradient>
    <linearGradient id="house-tones" x1="0" y1="0" x2="0" y2="1">
      <stop offset="0" stop-color="#d9dde3"/>
      <stop offset="0.45" stop-color="#8a6a58"/>
      <stop offset="0.7" stop-color="#b7b3ae"/>
      <stop offset="1" stop-color="#f4f6f9"/>
    </linearGradient>
    <linearGradient id="harbor-tones" x1="0" y1="0" x2="1" y2="1">
      <stop offset="0" stop-color="#3b2a6e"/>
      <stop offset="0.4" stop-color="#8a4a8f"/>
      <stop offset="0.7" stop-color="#5a3fa8"/>
      <stop offset="1" stop-color="#c0408f"/>
    </linearGradient>
    <linearGradient id="agent-tones" x1="0" y1="0" x2="0" y2="1">
      <stop offset="0" stop-color="#fbfcfe"/>
      <stop offset="0.35" stop-color="#6b4a3a"/>
      <stop offset="0.5" stop-color="#2a2a2e"/>
      <stop offset="1" stop-color="#1a1a1c"/>
    </linearGradient>
  </defs>

  <!-- card base -->
  <rect class="card" x="0" y="0" width="833" height="926" fill="var(--paper)"/>

  <!-- photo areas -->
  <polygon role="img" aria-label="Snow-covered brick colonial home exterior" points="410,60 478,0 745,0 802,178 690,255 470,255" fill="url(#house-tones)"/>
  <polygon role="img" aria-label="Waterfront at night with a lit Ferris wheel" points="553,323 801,180 833,225 833,462 706,584" fill="url(#harbor-tones)"/>
  <path role="img" aria-label="Portrait of the listing realtor" d="M0,420 C40,420 80,400 95,330 C110,320 190,320 200,340 C215,400 250,420 270,440 L272,605 L0,605 Z" fill="url(#agent-tones)"/>

  <!-- hero panel -->
  <polygon class="hero-panel" points="0,0 390,0 418,46 398,60 510,278 0,278" fill="url(#hero-blue)"/>
  <text class="headline" x="74" y="135" font-size="128" textLength="282" lengthAdjust="spacingAndGlyphs">FOR</text>
  <text class="headline" x="70" y="223" font-size="120" textLength="292" lengthAdjust="spacingAndGlyphs">SALE</text>
  <text class="presenting" x="216" y="242" text-anchor="middle">Presenting</text>
  <text class="address" x="216" y="264" text-anchor="middle">48207 Velmont Lane, Brandywine, MD</text>

  <!-- price band -->
  <polygon points="218,285 516,285 555,356 245,356" fill="var(--band-blue)"/>
  <text class="band-label" x="388" y="309" text-anchor="middle">Priced to Sell</text>
  <text class="price" x="390" y="340" text-anchor="middle" textLength="265" lengthAdjust="spacingAndGlyphs">Only $550,000</text>

  <!-- brokerage band -->
  <polygon points="308,362 553,362 590,416 330,416" fill="var(--band-blue)"/>
  <text class="brokerage" x="449" y="396" text-anchor="middle">Tolbrook Realty Inc.</text>

  <!-- email band -->
  <polygon points="249,423 590,423 622,470 249,470" fill="var(--band-blue)"/>
  <text class="email" x="433" y="452" text-anchor="middle">premierhomedesk@mailbrook.test</text>

  <!-- agent contact -->
  <text x="288" y="500"><tspan class="agent-name">Marcus Pendley,</tspan><tspan class="agent-title" dx="6">Realtor</tspan></text>
  <text class="agent-phone" x="288" y="533">Call: (240) 555-0187</text>
  <text class="brand-name" x="350" y="580">Tolbrook</text>
  <rect x="481" y="545" width="42" height="42" fill="var(--band-blue)"/>

  <!-- about property -->
  <rect x="0" y="610" width="833" height="294" fill="var(--panel-grey)"/>
  <rect x="0" y="605" width="833" height="10" fill="var(--band-blue)"/>
  <polygon points="0,605 282,605 262,650 0,650" fill="var(--band-blue)"/>
  <text class="section-title" x="42" y="635">ABOUT PROPERTY</text>

  <g class="features-left">
    <path class="tick" d="M43,692 l4,5 l8,-11"/>
    <text class="feature" x="62" y="697">5 Bedroom / 4 Bathroom Colonial with</text>
    <text class="feature" x="62" y="720">Contemporary Design and Charm</text>
    <path class="tick" d="M43,754 l4,5 l8,-11"/>
    <text class="feature" x="62" y="759">Over 5,000 sq ft of Spacious Elegance</text>
    <path class="tick" d="M43,794 l4,5 l8,-11"/>
    <text class="feature" x="62" y="799">Modern Open Concept Kitchen</text>
    <path class="tick" d="M43,834 l4,5 l8,-11"/>
    <text class="feature" x="62" y="839">Natural Oak Floors</text>
    <path class="tick" d="M43,874 l4,5 l8,-11"/>
    <text class="feature" x="62" y="879">Stainless Steel Appliances</text>
  </g>
  <g class="features-right">
    <path class="tick" d="M428,692 l4,5 l8,-11"/>
    <text class="feature" x="447" y="697">Extraordinary Master Bedroom with</text>
    <text class="feature" x="447" y="720">Spacious Bath</text>
    <path class="tick" d="M428,754 l4,5 l8,-11"/>
    <text class="feature" x="447" y="759">Granite Counter-Tops</text>
    <path class="tick" d="M428,794 l4,5 l8,-11"/>
    <text class="feature" x="447" y="799">Exterior with Outdoor Security, Design</text>
    <text class="feature" x="447" y="822">Lighting and Sprinkler System</text>
    <path class="tick" d="M428,857 l4,5 l8,-11"/>
    <text class="feature" x="447" y="862">Just 10 Minutes From Corwen Quay</text>
  </g>
</svg>
</body>
</html>
```